Harborline Network Solutions - IT Services Company/Managed Services/Consulting Card Design

Our company needs a business card design that will appeal to client companies with 50-1000 employees. We do IT services, administration, management, projects, budgeting and consulting (Like a small Quellbrook.com, Vantrelle.com or Drumvale.com). Mainly helping businesses use technology to be more competitive and efficient. We work with IT Infrastructure, switches, routers, firewalls and Cloud, Penwick/Tarvo servers, Kelpnode server virtualization, Datacenter environments, Email systems, Business Systems, Backup, Disaster Recovery, Data Security, ZPB, Workdesk 720 and Mistral.) Would like the final design to be professional but stand out to our prospective clients. Our current logo is attached. Color or design could be changed. Overall looking for a great finished product, original ideas are welcome and would pay more for the right one. If you think you have a better logo idea include a general idea if you can. Web design has not been done yet so that is a later possibility too.

Target Market(s)

1st - Mid-sized companies with 100-1000 employees with technology needs
2nd - Smaller companies with 20-99 employees with technology needs
- These companies can be in many different industries. Heathcare, legal, manufacturing, education, non-profit, services

Industry/Entity Type

Information Technology

Contact Information for Business Card

Should include the following info:

Logo or other logo with Company Name

Martin J. Calder

Principal

HarborlineNet.example

mcalder@HarborlineNet.example

(555) 7-HARBOR x 318

Font styles to use
Other font styles liked:
• designer can decide

Requirements
Must have
• Professional, appealing design, appeal to the target market
Nice to have
• Some sort of additional accent design that would stand out could be nice. I thought of adding a graphic in the top left corner that would look like the corner of the card was becoming more and more pixelated as it got near the corner, with some pixels missing.

```html
<!DOCTYPE html>
<html lang="en">
<head>
<meta charset="utf-8">
<title>Harborline Network Solutions – Business Card</title>
<link rel="stylesheet" href="https://fonts.googleapis.com/css2?family=Bitter:wght@400;500&display=swap">
<style>
  :root {
    --page-bg: #e9e7e4;
    --card-bg: #ffffff;
    --ink: #2a2a2c;
    --ink-soft: #3a3a3c;
    --brand-blue: #1f6fb8;
    --band-dark: #231f20;
    --accent-orange: #f08a3c;
    --accent-amber: #fbb040;
    --accent-teal: #27b2d6;
    --accent-sky: #8fd3ec;
    --accent-charcoal: #3b3d40;
  }
  * { box-sizing: border-box; margin: 0; padding: 0; }
  html, body { width: 1200px; height: 987px; overflow: hidden; }
  body {
    background: var(--page-bg);
    font-family: "Bitter", Georgia, serif;
    color: var(--ink);
    position: relative;
  }
  .card {
    position: absolute;
    left: 292px;
    width: 616px;
    height: 352px;
    background: var(--card-bg);
    overflow: hidden;
    box-shadow: 0 2px 8px rgba(0,0,0,0.18);
  }
  .card--front { top: 130px; }
  .card--back { top: 505px; height: 350px; }

  .pixel-corner {
    position: absolute; left: 0; top: 0; width: 320px; height: 210px;
    background: linear-gradient(135deg, var(--accent-amber) 0%, var(--accent-orange) 25%, var(--accent-teal) 50%, var(--accent-sky) 70%, rgba(143,211,236,0) 100%);
    clip-path: polygon(0 0, 100% 0, 55% 100%, 0 100%);
    opacity: 0.9;
  }
  .pixel-scatter {
    position: absolute; left: 0; top: 240px; width: 200px; height: 112px;
    background: linear-gradient(45deg, var(--accent-orange) 0%, var(--accent-charcoal) 25%, var(--accent-teal) 50%, rgba(143,211,236,0) 100%);
    clip-path: polygon(0 0, 100% 0, 0 100%);
    opacity: 0.85;
  }
  .swoosh { position: absolute; left: 0; top: 160px; width: 616px; height: 82px; }

  .brand {
    position: absolute;
    display: flex; align-items: center; gap: 10px;
    white-space: nowrap;
  }
  .brand__mark { width: 12px; height: 12px; background: var(--brand-blue); flex: none; }
  .brand__name {
    font-weight: 500; font-size: 25px; line-height: 1.15;
    color: var(--ink); text-align: center;
  }
  .card--front .brand { right: 40px; top: 44px; }
  .card--back .brand { left: 50%; top: 80px; transform: translateX(-50%); }

  .person { position: absolute; right: 40px; top: 183px; text-align: right; }
  .person__name { font-size: 21px; font-weight: 400; color: var(--ink); letter-spacing: 0.3px; }
  .person__title { font-size: 15px; color: var(--ink); margin-top: 2px; }

  .contact { position: absolute; right: 40px; top: 262px; list-style: none; text-align: right; }
  .contact__item {
    display: flex; justify-content: flex-end; align-items: center; gap: 10px;
    font-size: 14px; color: var(--ink-soft); height: 23px;
  }
  .contact__icon { width: 14px; height: 14px; fill: var(--brand-blue); flex: none; }

  .services-band {
    position: absolute; left: 0; bottom: 0; width: 100%; height: 114px;
    background: var(--band-dark);
    display: flex; flex-direction: column; justify-content: center; align-items: center;
  }
  .services-band p { color: #ffffff; font-size: 16px; line-height: 23.5px; }
  .pixel-cluster {
    position: absolute; left: 42px; top: 207px; width: 78px; height: 54px; z-index: 1;
    background: linear-gradient(135deg, var(--accent-charcoal) 0%, var(--brand-blue) 45%, var(--accent-amber) 75%, #ffffff 100%);
    clip-path: polygon(20% 0, 100% 30%, 100% 60%, 45% 100%, 0 60%);
  }
</style>
</head>
<body>

<section class="card card--front">
  <div class="pixel-corner" role="img" aria-label="Pixel mosaic accent dissolving into the top-left corner in orange, amber, teal, sky blue and charcoal squares"></div>
  <div class="pixel-scatter" role="img" aria-label="Scattered pixel squares in orange, teal and charcoal near the lower-left corner"></div>

  <svg class="swoosh" viewBox="0 0 616 82" preserveAspectRatio="none" aria-hidden="true">
    <defs>
      <linearGradient id="swooshFill" x1="0" x2="1" y1="0" y2="0">
        <stop offset="0" stop-color="#1e1e20"/>
        <stop offset="0.35" stop-color="#4b5a74"/>
        <stop offset="0.7" stop-color="#1f6fb8"/>
        <stop offset="1" stop-color="#1f6fb8" stop-opacity="0"/>
      </linearGradient>
    </defs>
    <polygon points="0,44 616,0 616,80 0,80" fill="url(#swooshFill)"/>
  </svg>

  <div class="brand">
    <span class="brand__mark"></span>
    <span class="brand__name">Harborline<br>Network Solutions</span>
  </div>

  <div class="person">
    <div class="person__name">Martin J. Calder</div>
    <div class="person__title">Principal</div>
  </div>

  <ul class="contact">
    <li class="contact__item">(555) 7-HARBOR x 318
      <svg class="contact__icon" viewBox="0 0 24 24" aria-hidden="true"><path d="M6.6 10.8a15.2 15.2 0 0 0 6.6 6.6l2.2-2.2a1 1 0 0 1 1-.25 11.4 11.4 0 0 0 3.6.57 1 1 0 0 1 1 1V20a1 1 0 0 1-1 1A17 17 0 0 1 3 4a1 1 0 0 1 1-1h3.5a1 1 0 0 1 1 1c0 1.25.2 2.45.57 3.57a1 1 0 0 1-.25 1z"/></svg>
    </li>
    <li class="contact__item">mcalder@HarborlineNet.example
      <svg class="contact__icon" viewBox="0 0 24 24" aria-hidden="true"><path d="M2 5h20v14H2z M3.5 6.5v1l8.5 5.5 8.5-5.5v-1l-8.5 5.5z" fill-rule="evenodd"/></svg>
    </li>
    <li class="contact__item">www.HarborlineNet.example
      <svg class="contact__icon" viewBox="0 0 24 24" aria-hidden="true"><circle cx="12" cy="12" r="10"/><path d="M12 2v20M2 12h20M5 6.5c4 2 10 2 14 0M5 17.5c4-2 10-2 14 0" stroke="#fff" stroke-width="1.4" fill="none"/></svg>
    </li>
  </ul>
</section>

<section class="card card--back">
  <div class="brand">
    <span class="brand__mark"></span>
    <span class="brand__name">Harborline<br>Network Solutions</span>
  </div>

  <div class="pixel-cluster" role="img" aria-label="Small cluster of blue, black, orange and white pixel squares"></div>

  <div class="services-band">
    <p>IT Services – Administration – Management</p>
    <p>Projects – IT Security – Budgeting – Consulting</p>
    <p>Infrastructure – Cloud/Hybrid – VoIP</p>
  </div>
</section>

</body>
</html>
```